Business Cards Needed

Hi designers, I have a new logo that was created by one of the PixelHarbor designers. I'd now like to use that logo to make business cards. The company is called CarewiseMetrics Advisory and is a business consulting firm. I'd like the business cards to be horizontal, modern, and professional.
I'd like the following information to be on the business card:
1) Logo
2) my name - Janine Oulton
3) my title - Principal
4) name of business - CarewiseMetrics Advisory
5) mobile - 508.742.3391
6) e-mail - janine@carewisemetricsadvisory.example
I'm uploading a JPG file of the logo. I'm hoping this is the correct file format. Please let me know if you need another type of file. Thank you.

```html
<!DOCTYPE html>
<html lang="en">
<head>
<meta charset="utf-8">
<title>CarewiseMetrics Advisory – Business Card</title>
<link href="https://fonts.googleapis.com/css2?family=Montserrat:wght@400;500;700&display=swap" rel="stylesheet">
<style>
  :root {
    --backdrop: #d4d5d7;
    --brand-blue: #1475bc;
    --brand-green: #8dc13f;
    --paper: #ffffff;
  }
  html, body {
    margin: 0;
    padding: 0;
    width: 900px;
    height: 1200px;
    overflow: hidden;
    background: var(--backdrop);
    font-family: "Montserrat", Arial, sans-serif;
  }
  .card {
    position: absolute;
    width: 630px;
    height: 360px;
    overflow: hidden;
  }
  .card--front {
    left: 135px;
    top: 213px;
    background: var(--brand-blue);
    display: flex;
    align-items: center;
    justify-content: center;
  }
  .front-wordmark {
    color: var(--paper);
    font-weight: 500;
    font-size: 31px;
    letter-spacing: 0.2px;
    margin: 0;
  }
  .card--back {
    left: 136px;
    top: 627px;
    background: var(--paper);
  }
  .side-panel {
    position: absolute;
    top: 0;
    right: 0;
    width: 130px;
    height: 100%;
    background: var(--brand-blue);
  }
  .side-stripe {
    position: absolute;
    top: 0;
    right: 142px;
    width: 10px;
    height: 100%;
    background: var(--brand-green);
  }
  .back-wordmark {
    position: absolute;
    left: 44px;
    top: 62px;
    margin: 0;
    color: var(--brand-blue);
    font-weight: 500;
    font-size: 21px;
  }
  .holder-name {
    position: absolute;
    left: 44px;
    top: 184px;
    margin: 0;
    color: var(--brand-green);
    font-weight: 700;
    font-size: 26px;
    line-height: 32px;
    letter-spacing: 0.3px;
  }
  .holder-title {
    position: absolute;
    left: 44px;
    top: 214px;
    margin: 0;
    color: var(--brand-blue);
    font-size: 15px;
    line-height: 20px;
    letter-spacing: 0.6px;
  }
  .title-rule {
    position: absolute;
    left: 44px;
    top: 240px;
    width: 73px;
    height: 2px;
    background: var(--brand-green);
  }
  .contact-list {
    position: absolute;
    left: 44px;
    top: 252px;
    margin: 0;
    padding: 0;
    list-style: none;
  }
  .contact-item {
    display: flex;
    align-items: center;
    height: 24px;
    color: var(--brand-blue);
    font-size: 13px;
    letter-spacing: 0.3px;
  }
  .contact-item--phone { letter-spacing: 1.8px; font-size: 15px; }
  .contact-icon {
    width: 14px;
    height: 14px;
    margin-right: 7px;
    flex: none;
  }
</style>
</head>
<body>

<section class="card card--front" aria-label="Card front">
  <p class="front-wordmark">CarewiseMetrics Advisory</p>
</section>

<section class="card card--back" aria-label="Card back">
  <div class="side-stripe" aria-hidden="true"></div>
  <div class="side-panel" aria-hidden="true"></div>

  <p class="back-wordmark">CarewiseMetrics Advisory</p>

  <h1 class="holder-name">JANINE OULTON</h1>
  <p class="holder-title">Principal</p>
  <div class="title-rule"></div>

  <ul class="contact-list">
    <li class="contact-item contact-item--phone">
      <svg class="contact-icon" viewBox="0 0 24 24" aria-hidden="true"><path fill="var(--brand-green)" d="M6.6 10.8a15.1 15.1 0 0 0 6.6 6.6l2.2-2.2c.3-.3.7-.4 1-.2 1.1.4 2.3.6 3.6.6.6 0 1 .4 1 1V20c0 .6-.4 1-1 1C10.6 21 3 13.4 3 4c0-.6.4-1 1-1h3.5c.6 0 1 .4 1 1 0 1.3.2 2.5.6 3.6.1.3 0 .7-.2 1z"/></svg>
      508.742.3391
    </li>
    <li class="contact-item">
      <svg class="contact-icon" viewBox="0 0 24 24" aria-hidden="true"><rect x="2" y="5" width="20" height="14" fill="var(--brand-green)"/><path d="M2 5 L12 13 L22 5" fill="none" stroke="#fff" stroke-width="1.6"/></svg>
      janine@carewisemetricsadvisory.example
    </li>
    <li class="contact-item">
      <svg class="contact-icon" viewBox="0 0 24 24" aria-hidden="true"><g fill="none" stroke="var(--brand-green)" stroke-width="1.8"><circle cx="12" cy="12" r="9.5"/><ellipse cx="12" cy="12" rx="4.2" ry="9.5"/><path d="M2.5 12h19M4 7h16M4 17h16"/></g></svg>
      www.carewisemetricsadvisory.example
    </li>
  </ul>
</section>

</body>
</html>
```